Modern luxury trendy cosmetics label

Looking for a cosmetics packaging label design. We are looking for a professionel, modern and luxury look like Lorena Vasquel, Meadowkin Apothecary, Marigold Tessin, Gavin Albert Pruke, Zuna, Orvik + Dalle, Velumi, Sleepy Walrus, the plainfold, lumiere de sable.Name of product: Nordic Tulip Mask - Needle-Free Contour Ritual Ingredients that have scientific proof of anti aging: Cherry blossom extact, collegen, hyaluronic acid, coconut oil. Color of product itself: Pastel pink. Smell: Cherry blossom. Colors of label: simple and black and white or some subtle colors.

Target Market(s)

Women, luxury market, modern women, young and old women

Industry/Entity Type

Cosmetics

Font styles to use
Sans Serif

Colors

Designer to choose colors to be used in the design.

Requirements
Must have
• A modern look, professional, cosmetics, beauty, professional market, original

```html
<!DOCTYPE html>
<html lang="en">
<head>
<meta charset="utf-8">
<title>Ovela Nordic Tulip Mask Label</title>
<link rel="stylesheet" href="https://fonts.googleapis.com/css2?family=Figtree:wght@300;400;500&display=swap">
<style>
  :root {
    --label-pink-light: #f6e1e6;
    --label-pink-mid: #ecd5da;
    --label-pink-deep: #e6cdd3;
    --ink: #111111;
    --illustration-tone: #b89aa2;
  }
  * { margin: 0; padding: 0; box-sizing: border-box; }
  html, body {
    width: 1094px;
    height: 1200px;
    overflow: hidden;
  }
  body {
    font-family: "Figtree", "Helvetica Neue", Arial, sans-serif;
    color: var(--ink);
    background: linear-gradient(90deg, var(--label-pink-light) 0%, var(--label-pink-mid) 55%, var(--label-pink-deep) 100%);
  }
  .label {
    position: relative;
    width: 1094px;
    height: 1200px;
  }
  .brand-name {
    position: absolute;
    left: 372px;
    top: 528px;
    height: 290px;
    writing-mode: vertical-rl;
    transform: rotate(180deg);
    font-size: 150px;
    font-weight: 400;
    line-height: 0.82;
    letter-spacing: -2px;
    text-align: center;
  }
  .divider-vertical {
    position: absolute;
    left: 517px;
    top: 610px;
    width: 2px;
    height: 203px;
    background: var(--ink);
  }
  .blossom-branch {
    position: absolute;
    left: 518px;
    top: 420px;
    width: 200px;
    height: 198px;
    background: linear-gradient(215deg, var(--illustration-tone) 0%, rgba(184,154,162,0.35) 100%);
    border-radius: 2px;
  }
  .product-title {
    position: absolute;
    left: 543px;
    top: 622px;
    font-size: 40px;
    font-weight: 500;
    line-height: 49px;
  }
  .title-rule {
    position: absolute;
    left: 543px;
    top: 777px;
    width: 202px;
    height: 1px;
    background: var(--ink);
  }
  .product-type {
    position: absolute;
    left: 543px;
    top: 789px;
    font-size: 25px;
    font-weight: 400;
    letter-spacing: 0.3px;
  }
  .product-volume {
    position: absolute;
    left: 543px;
    top: 850px;
    font-size: 16px;
    font-weight: 400;
  }
</style>
</head>
<body>
  <main class="label">
    <div class="brand-name">ovela</div>
    <div class="divider-vertical"></div>
    <div class="blossom-branch" role="img" aria-label="Black silhouette of a flowering tulip branch rising from the divider line"></div>
    <h1 class="product-title">Nordic<br>Tulip<br>Mask</h1>
    <div class="title-rule"></div>
    <p class="product-type">anti-aging cream</p>
    <p class="product-volume">50 mL / 1.6907 fl. oz</p>
  </main>
</body>
</html>
```